Commercial Construction Interior Fitout company needs Logo and Business Cards

We need a logo and business card design. We specialise in Commercial Ceilings, Partitions, Plastering and Carpentry.

Company name: 7QX Commercial Interiors. Would like a professional looking card more than a fancy look. Gloss front preferably black pattern with Fluro Green and white text.

Will need:

Name
Position
Phone
Fax
Email
Postal Address
Web address
Updates

Thank you so much everyone for your efforts and fantastic designs..   If I didn't respond to everyone personally,  my apologises. 

Again, thanks all

R.M                               

Target Market(s)

Existing & New clients in the Construction Industry

Industry/Entity Type

Business

Requirements
Nice to have
• 7QX to be overlapped or made into some sort of Logo

```html
<!DOCTYPE html>
<html lang="en">
<head>
<meta charset="utf-8">
<title>7QX Commercial Interiors – Business Cards</title>
<link rel="stylesheet" href="https://fonts.googleapis.com/css2?family=Oswald:wght@500&family=Poiret+One&family=Mulish:wght@400;700;800&family=Questrial&display=swap">
<style>
  :root {
    --card-dark: #2b2b2b;
    --card-dark-2: #333333;
    --sheen: #5a5a5a;
    --fluro-green: #43ad4a;
    --white: #ffffff;
    --label-grey: #333333;
    --page: #ffffff;
  }
  * { box-sizing: border-box; margin: 0; padding: 0; }
  html, body { width: 1200px; height: 865px; overflow: hidden; background: var(--page); }
  body { position: relative; font-family: "Questrial", sans-serif; }

  .option-label {
    position: absolute; top: 34px; font: 22px "Questrial", sans-serif; color: var(--label-grey);
  }
  .option-label--one { left: 314px; }
  .option-label--two { left: 853px; }

  .card {
    position: absolute; width: 507px; height: 317px; border-radius: 24px; overflow: hidden;
    background: var(--card-dark);
    box-shadow: 0 10px 28px rgba(0,0,0,.28);
  }
  .card--gloss {
    background: linear-gradient(125deg, var(--card-dark) 0%, var(--card-dark-2) 30%, var(--sheen) 52%, var(--card-dark-2) 66%, var(--card-dark) 100%);
  }
  .card--gloss-front { left: 73px; top: 117px; }
  .card--gloss-back { left: 67px; top: 506px; width: 506px; height: 316px; }
  .card--band-front { left: 641px; top: 117px; }
  .card--band-back { left: 641px; top: 505px; }

  .green-band { position: absolute; left: 0; right: 0; bottom: 0; height: 24px; background: var(--fluro-green); }

  /* Gloss front */
  .brand-mark {
    position: absolute; left: 0; right: 0; text-align: center;
    font-family: "Oswald", sans-serif; font-weight: 500; color: var(--fluro-green);
  }
  .card--gloss-front .brand-mark--code { top: 100px; font-size: 58px; line-height: 1; letter-spacing: 2px; }
  .card--gloss-front .rule { position: absolute; left: 63px; width: 369px; top: 172px; height: 5px; background: var(--fluro-green); }
  .card--gloss-front .brand-mark--name { top: 188px; font-size: 38px; line-height: 1.1; }

  /* Gloss back */
  .card--gloss-back .brand-mark--code { left: 38px; right: auto; width: 174px; top: 38px; font-size: 32px; line-height: 1; }
  .card--gloss-back .rule { position: absolute; left: 38px; width: 174px; top: 83px; height: 3px; background: var(--fluro-green); }
  .card--gloss-back .brand-mark--name { left: 38px; right: auto; width: 174px; top: 90px; font-size: 17px; line-height: 1.2; }

  /* Band front */
  .card--band-front .brand-mark--code {
    top: 118px; font-family: "Mulish", sans-serif; font-weight: 800; font-size: 60px; line-height: 1; color: var(--white);
  }
  .deco-name {
    position: absolute; left: 0; right: 0; text-align: center;
    font-family: "Poiret One", sans-serif; color: var(--fluro-green); letter-spacing: 2px; white-space: nowrap;
  }
  .card--band-front .deco-name { top: 192px; font-size: 36px; line-height: 1.1; }
  .card--band-back .deco-name { top: 50px; font-size: 34px; line-height: 1.1; }

  /* Contact blocks */
  .holder {
    position: absolute; text-align: right; font-family: "Mulish", sans-serif; color: var(--white); font-size: 18px; line-height: 23px;
  }
  .holder__name { font-weight: 700; }
  .holder__position { font-weight: 400; }
  .divider { position: absolute; width: 2px; background: var(--fluro-green); }
  .contact-list { position: absolute; list-style: none; color: var(--white); font-size: 18.5px; }
  .contact-list li { display: flex; align-items: center; height: 29.5px; }
  .contact-list svg { width: 17px; height: 17px; margin-right: 8px; flex: none; }

  .card--gloss-back .holder { right: 314px; top: 163px; }
  .card--gloss-back .divider { left: 209px; top: 129px; height: 146px; }
  .card--gloss-back .contact-list { left: 222px; top: 126px; }

  .card--band-back .holder { right: 281px; top: 134px; }
  .card--band-back .divider { left: 243px; top: 105px; height: 136px; }
  .card--band-back .contact-list { left: 256px; top: 97px; }
</style>
</head>
<body>
  <div class="option-label option-label--one">1</div>
  <div class="option-label option-label--two">2</div>

  <!-- Option 1 -->
  <section class="card card--gloss card--gloss-front" aria-label="Option 1 card front">
    <div class="brand-mark brand-mark--code">7QX</div>
    <div class="rule"></div>
    <div class="brand-mark brand-mark--name">COMMERCIAL INTERIORS</div>
  </section>

  <section class="card card--gloss card--gloss-back" aria-label="Option 1 card back">
    <div class="brand-mark brand-mark--code">7QX</div>
    <div class="rule"></div>
    <div class="brand-mark brand-mark--name">COMMERCIAL INTERIORS</div>
    <div class="holder"><div class="holder__name">Your Name</div><div class="holder__position">Position</div></div>
    <div class="divider"></div>
    <ul class="contact-list">
      <li><svg viewBox="0 0 16 16"><path fill="#fff" d="M3.5 1l2.5 3-1.6 1.6c.9 2 2.5 3.6 4.5 4.5L10.5 8.5l3 2.5-1.3 2.6C7 13.5 2.5 9 2.4 3.8z"/></svg>012 345 6789</li>
      <li><svg viewBox="0 0 16 16"><path fill="none" stroke="#fff" stroke-width="1.4" d="M4 2h7v4H4zM2 6h12v6H2zM4 12h8v3H4z"/></svg>023 456 7800</li>
      <li><svg viewBox="0 0 16 16"><path fill="none" stroke="#fff" stroke-width="1.4" d="M1.5 3.5h13v9h-13zM1.5 3.5l6.5 5 6.5-5"/></svg>name@7qxmail.com</li>
      <li><svg viewBox="0 0 16 16"><path fill="#fff" d="M8 4C4.5 4 2 8 2 8s2.5 4 6 4 6-4 6-4-2.5-4-6-4zm0 6.3A2.3 2.3 0 1 1 8 5.7a2.3 2.3 0 0 1 0 4.6z"/></svg>Postal Address</li>
      <li><svg viewBox="0 0 16 16"><g fill="none" stroke="#fff" stroke-width="1.2"><circle cx="8" cy="8" r="6.3"/><ellipse cx="8" cy="8" rx="2.8" ry="6.3"/><path d="M1.7 8h12.6M2.6 5h10.8M2.6 11h10.8"/></g></svg>www.7qx.com</li>
    </ul>
  </section>

  <!-- Option 2 -->
  <section class="card card--band-front" aria-label="Option 2 card front">
    <div class="brand-mark brand-mark--code">7QX</div>
    <div class="deco-name">COMMERCIAL INTERIORS</div>
    <div class="green-band"></div>
  </section>

  <section class="card card--band-back" aria-label="Option 2 card back">
    <div class="deco-name">COMMERCIAL INTERIORS</div>
    <div class="holder"><div class="holder__name">Your Name</div><div class="holder__position">Position</div></div>
    <div class="divider"></div>
    <ul class="contact-list">
      <li><svg viewBox="0 0 16 16"><path fill="#fff" d="M3.5 1l2.5 3-1.6 1.6c.9 2 2.5 3.6 4.5 4.5L10.5 8.5l3 2.5-1.3 2.6C7 13.5 2.5 9 2.4 3.8z"/></svg>012 345 6789</li>
      <li><svg viewBox="0 0 16 16"><path fill="none" stroke="#fff" stroke-width="1.4" d="M4 2h7v4H4zM2 6h12v6H2zM4 12h8v3H4z"/></svg>023 456 7800</li>
      <li><svg viewBox="0 0 16 16"><path fill="none" stroke="#fff" stroke-width="1.4" d="M1.5 3.5h13v9h-13zM1.5 3.5l6.5 5 6.5-5"/></svg>name@7qxmail.com</li>
      <li><svg viewBox="0 0 16 16"><path fill="#fff" d="M8 4C4.5 4 2 8 2 8s2.5 4 6 4 6-4 6-4-2.5-4-6-4zm0 6.3A2.3 2.3 0 1 1 8 5.7a2.3 2.3 0 0 1 0 4.6z"/></svg>Postal Address</li>
      <li><svg viewBox="0 0 16 16"><g fill="none" stroke="#fff" stroke-width="1.2"><circle cx="8" cy="8" r="6.3"/><ellipse cx="8" cy="8" rx="2.8" ry="6.3"/><path d="M1.7 8h12.6M2.6 5h10.8M2.6 11h10.8"/></g></svg>www.7qx.com</li>
    </ul>
    <div class="green-band"></div>
  </section>
</body>
</html>
```